Business cards for Veterinarian
Dale Forsk, DVM
Project: Business cards for Veterinarian
Business cards for Veterinarian -
Creative Brief
Use specific fonts
Whatever works, but not curly twisty stuff that is hard to read!
Bright & Fun-filled
872 Hollin Parkway Brunswick, GA 31587
info@daleforskvet.example
daleforskvet.example
I'm thinking the front would be mostly logo and phone number and put the rest of the info on the back, just so you can see the logo/phone number better, basically..... Would also like "Located across from the QMRL" on there somewhere, as well as "Office Hours By Appointment" Could put the veterinary caduceus on there and, if room allowed, some sort of a line or something to write the time of the next appointment (may not be enough room for that - if not, no big deal.) I kinda like watermarks too, if you wanted to try something with them.

```html
<!DOCTYPE html>
<html lang="en">
<head>
<meta charset="utf-8">
<title>Dale Forsk, DVM — Business Card</title>
<link rel="stylesheet" href="https://fonts.googleapis.com/css2?family=Source+Sans+3:ital,wght@0,300;0,400;1,400&display=swap">
<style>
  :root {
    --card-edge: #090909;
    --card-center: #272727;
    --stripe-light: rgba(255, 255, 255, 0.022);
    --stripe-dark: rgba(0, 0, 0, 0.05);
    --text-main: #f4f4f4;
    --text-soft: #e8e8e8;
    --accent-teal: #45c6cf;
    --divider: rgba(255, 255, 255, 0.11);
  }
  html, body {
    margin: 0;
    padding: 0;
    width: 1200px;
    height: 695px;
    overflow: hidden;
    background: var(--card-edge);
  }
  .card {
    position: relative;
    width: 1200px;
    height: 695px;
    overflow: hidden;
    font-family: "Source Sans 3", "Myriad Pro", Arial, sans-serif;
    background:
      repeating-linear-gradient(90deg, var(--stripe-light) 0 3px, var(--stripe-dark) 3px 6px),
      radial-gradient(ellipse 70% 80% at 50% 50%, var(--card-center) 0%, #171717 55%, var(--card-edge) 100%);
  }
  .identity {
    position: absolute;
    right: 652px;
    top: 290px;
    text-align: right;
  }
  .identity__name {
    margin: 0;
    font-weight: 300;
    font-size: 70px;
    line-height: 70px;
    color: var(--text-main);
    letter-spacing: -0.5px;
  }
  .identity__title {
    margin: 10px 0 0;
    font-weight: 300;
    font-size: 31px;
    line-height: 31px;
    color: var(--text-main);
    letter-spacing: 1px;
  }
  .divider {
    position: absolute;
    left: 599px;
    top: 266px;
    width: 1px;
    height: 168px;
    background: var(--divider);
  }
  .contact {
    position: absolute;
    left: 643px;
    top: 322px;
    margin: 0;
    padding: 0;
    list-style: none;
    font-size: 18px;
    line-height: 25px;
    color: var(--text-soft);
  }
  .contact__label {
    font-style: italic;
    color: var(--accent-teal);
  }
  .contact__value--italic {
    font-style: italic;
  }
  .contact__indent {
    display: block;
    padding-left: 72px;
    font-style: italic;
  }
</style>
</head>
<body>
  <main class="card">
    <header class="identity">
      <h1 class="identity__name">Dale Forsk</h1>
      <p class="identity__title">DVM</p>
    </header>
    <div class="divider" aria-hidden="true"></div>
    <ul class="contact">
      <li><span class="contact__label">info@</span> daleforskvet.example</li>
      <li><span class="contact__label">website:</span> <span class="contact__value--italic">www.daleforskvet.example</span></li>
      <li><span class="contact__label">address:</span> <span class="contact__value--italic">872 Hollin Parkway</span>
        <span class="contact__indent">Brunswick, GA 31587</span></li>
    </ul>
  </main>
</body>
</html>
```